Business Card Design for company

We want new business cards. We'd like something different-- yet still highly professional. Our tagline is Providing leadership, delivering success. Stock photos are ok, as long as they are relevant and look upscale.

Target Market(s)

Architecture/Business Management Consulting/Engineering Consulting

Contact Information for Business Card

dark gray background with pops of blue might be good, but you tell me. You're the designers. Rounded corners might be nice, but again, you tell me.

Font styles to use
Serif
Sans Serif

Colors
3276b5
5c5c5c
9d9d9d
fbfbfb

Requirements
Nice to have
• Something different, but still very professional.

```html
<!DOCTYPE html>
<html lang="en">
<head>
<meta charset="utf-8">
<title>Veltra Group – Business Card</title>
<link rel="stylesheet" href="https://fonts.googleapis.com/css2?family=Montserrat:wght@300;400;600;700&display=swap">
<style>
  :root {
    --page: #ffffff;
    --card: #b5b5b5;
    --blue: #3276b5;
    --band: #7f9cb6;
    --soft: #9ba8b6;
    --icon-cut: #b5b5b5;
  }
  html, body {
    margin: 0;
    width: 1200px;
    height: 1200px;
    overflow: hidden;
    background: var(--page);
    font-family: "Montserrat", Arial, sans-serif;
  }
  .canvas {
    position: relative;
    width: 1200px;
    height: 1200px;
  }
  .card {
    position: absolute;
    left: 290px;
    width: 672px;
    height: 374px;
    display: block;
  }
  .card--front { top: 158px; }
  .card--back  { top: 610px; }
  .card-bg { fill: var(--card); }
  .band { fill: var(--band); }
  .gradient-soft { stop-color: var(--soft); }
  .gradient-blue { stop-color: var(--blue); }
  .brand-name {
    fill: var(--blue);
    font-weight: 700;
    font-size: 50px;
    letter-spacing: 2px;
  }
  .divider { fill: var(--blue); }
  .person-name { fill: var(--blue); font-weight: 600; font-size: 56px; }
  .person-role { fill: var(--blue); font-weight: 600; font-size: 25px; letter-spacing: 1px; }
  .contact-text { fill: var(--blue); font-weight: 300; font-size: 24px; }
  .icon { fill: var(--blue); }
  .icon-line { fill: none; stroke: var(--blue); stroke-width: 2; }
  .icon-cut { fill: none; stroke: var(--icon-cut); stroke-width: 2; }
</style>
</head>
<body>
<main class="canvas">

  <svg class="card card--front" viewBox="0 0 840 467" aria-label="Business card front">
    <defs>
      <linearGradient id="accent-fade" x1="0" y1="0" x2="0" y2="1">
        <stop class="gradient-soft" offset="0"/>
        <stop class="gradient-blue" offset="1"/>
      </linearGradient>
    </defs>
    <rect class="card-bg" width="840" height="467"/>
    <rect class="band" x="0" y="450" width="840" height="17"/>
    <rect class="corner-accent" x="0" y="328" width="143" height="139" fill="url(#accent-fade)" role="img" aria-label="Decorative blue accent, lower left corner"/>
    <rect class="corner-accent" x="697" y="328" width="143" height="139" fill="url(#accent-fade)" role="img" aria-label="Decorative blue accent, lower right corner"/>
    <text class="brand-name" x="420" y="258" text-anchor="middle">VELTRA GROUP</text>
  </svg>

  <svg class="card card--back" viewBox="0 0 840 467" aria-label="Business card back">
    <defs>
      <linearGradient id="accent-fade-back" x1="0" y1="0" x2="1" y2="1">
        <stop class="gradient-soft" offset="0"/>
        <stop class="gradient-blue" offset="1"/>
      </linearGradient>
    </defs>
    <rect class="card-bg" width="840" height="467"/>
    <rect class="band" x="0" y="410" width="840" height="57"/>
    <rect class="corner-accent" x="544" y="308" width="296" height="159" fill="url(#accent-fade-back)" role="img" aria-label="Decorative blue accent, lower right corner"/>

    <text class="person-name" x="227" y="238" text-anchor="middle">YourName</text>
    <text class="person-role" x="220" y="268" text-anchor="middle">POSITON</text>

    <rect class="divider" x="412" y="104" width="5" height="258"/>

    <g class="contact">
      <path class="icon" d="M505 170 l14 12 h-4 v11 h-7 v-7 h-6 v7 h-7 v-11 h-4 z"/>
      <text class="contact-text" x="538" y="193">Your Address</text>

      <circle class="icon-line" cx="503" cy="218" r="11"/>
      <ellipse class="icon-line" cx="503" cy="218" rx="5" ry="11"/>
      <line class="icon-line" x1="492" y1="218" x2="514" y2="218"/>
      <text class="contact-text" x="536" y="227">Yourwebsite.com</text>

      <path class="icon" d="M507 239 l6 4 -3 6 c-2 6 -8 12 -16 12 l-3 -1 3 -6 c4 0 8 -3 10 -8 z"/>
      <text class="contact-text" x="531" y="257">00 0000 0000</text>

      <rect class="icon" x="490" y="277" width="26" height="17" rx="2"/>
      <path class="icon-cut" d="M491 279 l12 9 12 -9"/>
      <text class="contact-text" x="527" y="292">Youremail@email.com</text>
    </g>
  </svg>

</main>
</body>
</html>
```